International Parcel Forwarder needs website redesign and logo

We need an updated website design to make our existing site look more modern, global and trustworthy. Current site
www.parvento.com -- we do not want to rebuild headers or at this point do copyright we are simply looking to make the site pop:)
The service we provide is for shoppers living outside the USA looking to shop here and save money on shipping or get access to stores that won't ship internationally or accept international payment.
Target Market(s)
Online shoppers living outside the USA
Industry/Entity Type
Shipping
Logo Text
US shopping, global shipping
Coding
Coded - Design and coding required
Number of Pages Required
5+ page
Font styles to use

```html
<!DOCTYPE html>
<html lang="en">
<head>
<meta charset="utf-8">
<title>Parvento — US shopping, global shipping</title>
<link rel="stylesheet" href="https://fonts.googleapis.com/css2?family=Montserrat:wght@400;500;600;700&family=Open+Sans:wght@400;600&display=swap">
<style>
:root{
  --navy:#1f2833;
  --navy-2:#252f3b;
  --orange:#f7941d;
  --blue:#3d7fc4;
  --sky:#1aa6e4;
  --card:#eef1f4;
  --ink:#222a33;
  --muted:#7b8490;
  --white:#ffffff;
  --line:#4a5663;
}
*{box-sizing:border-box;margin:0;padding:0}
html,body{width:1200px;height:3136px;overflow:hidden}
body{position:relative;background:var(--white);font-family:"Open Sans",Arial,sans-serif;color:var(--ink)}
.abs{position:absolute}
h1,h2,h3,.heading{font-family:"Montserrat",Arial,sans-serif}
.divider{display:block;width:44px;border-top:3px dotted var(--ink);margin:10px auto 0}

/* top bar */
.topbar{left:0;top:0;width:1200px;height:38px;background:var(--navy);color:#c9d0d8;font-size:12px;font-family:"Montserrat",sans-serif}
.topbar .contact{left:155px;top:12px;display:flex;gap:14px;align-items:center}
.topbar .account{right:155px;top:12px;display:flex;gap:12px;align-items:center}
.topbar .social{display:flex;gap:8px}
.topbar .social span{width:10px;height:10px;border-radius:50%;background:#c9d0d8;display:block}
.topbar .social span.hot{background:var(--orange)}

/* header */
.header{left:0;top:38px;width:1200px;height:84px;background:var(--navy-2)}
.logo{left:155px;top:18px;color:var(--white)}
.logo .name{display:flex;align-items:center;gap:8px;font-family:"Montserrat",sans-serif;font-weight:700;font-size:28px;line-height:1}
.logo .name i{width:20px;height:20px;background:var(--white);display:block}
.logo .tag{font-size:11px;margin-top:6px;color:#d7dde3}
.nav{right:155px;top:34px;display:flex;gap:26px;font-family:"Montserrat",sans-serif;font-size:13px;color:var(--white)}
.nav a{color:inherit;text-decoration:none;position:relative}
.nav a.active{color:var(--orange)}
.nav a.active::after{content:"";position:absolute;left:50%;top:38px;margin-left:-8px;border:8px solid transparent;border-bottom-color:var(--orange)}

/* hero */
.hero{left:0;top:122px;width:1200px;height:447px;overflow:hidden}
.hero .photo{left:0;top:0;width:1200px;height:447px;background:linear-gradient(180deg,#2d4a78 0%,#4d6f9d 45%,#7b8fae 70%,#36476a 100%)}
.hero .tint{left:0;top:0;width:600px;height:447px;background:rgba(58,122,196,.88)}
.hero .frame{left:372px;top:125px;width:228px;height:210px;border:3px solid rgba(255,255,255,.35)}
.hero h1{left:155px;top:135px;color:var(--white);font-size:50px;font-weight:600}
.hero p{left:155px;top:203px;width:440px;color:var(--white);font-size:16px;line-height:20px}
.hero p b{color:var(--ink)}
.btn-orange{background:var(--orange);color:var(--white);font-family:"Montserrat",sans-serif;font-size:13px;text-align:center;display:block}
.hero .cta{left:160px;top:270px;width:128px;height:32px;line-height:32px}
.hero .arrow{width:36px;height:36px;border-radius:50%;top:206px;display:flex;align-items:center;justify-content:center}
.hero .arrow.prev{left:70px;border:2px solid rgba(255,255,255,.6)}
.hero .arrow.next{left:1090px;background:var(--orange)}

/* how it works */
.section-title{left:0;width:1200px;text-align:center;font-size:23px;font-weight:500;color:var(--ink)}
.steps{left:155px;top:721px;display:flex;gap:26px}
.step{position:relative;width:203px;height:201px;background:var(--card);text-align:center;font-size:12px;line-height:17px;color:#3a434d}
.step.featured{background:var(--orange);color:var(--white)}
.step .icon{width:72px;height:72px;border-radius:50%;background:var(--blue);margin:28px auto 18px;display:flex;align-items:center;justify-content:center}
.step.featured .icon{background:transparent;border:3px solid var(--white)}
.step p{padding:0 24px}
.step .dot{position:absolute;left:50%;bottom:-10px;margin-left:-10px;width:20px;height:20px;border-radius:50%;background:var(--navy);border:3px solid var(--white)}
.step.featured .dot{background:var(--orange)}

/* story */
.story-text{left:165px;top:1058px;width:380px;text-align:center}
.story-text h2{font-size:23px;font-weight:600}
.story-text p{margin-top:26px;font-size:12.5px;line-height:18px;color:var(--muted)}
.btn-outline{display:inline-block;border:2px solid var(--orange);color:var(--ink);font-family:"Montserrat",sans-serif;font-size:12px;padding:7px 18px;margin-top:26px}
.story-media{left:610px;top:1018px;width:433px;height:351px;background:radial-gradient(circle at 50% 50%,#2f64b4 0 36%,#c9a52a 37%,#9c7a12 100%)}
.play{left:803px;top:1167px;width:48px;height:48px;border-radius:50%;border:3px solid var(--white);display:flex;align-items:center;justify-content:center}

/* why */
.why-photo{left:0;top:1448px;width:600px;height:538px;background:linear-gradient(180deg,#3a6d9a 0%,#f0a54a 45%,#c9884a 62%,#5d5450 100%)}
.why-panel{left:600px;top:1448px;width:600px;height:538px;background:var(--sky)}
.why-panel h2{position:absolute;left:63px;top:60px;color:var(--white);font-size:23px;font-weight:500}
.why-panel .divider{position:absolute;left:63px;top:98px;margin:0;border-color:var(--white)}
.reason{position:absolute;left:63px;color:var(--white)}
.reason h3{font-size:15px;font-weight:600}
.reason p{font-size:12px;margin-top:8px}
.why-icon{width:62px;height:62px;border-radius:50%;background:var(--white);border:3px solid var(--sky);display:flex;align-items:center;justify-content:center;left:569px}
.why-icon.hot{background:var(--orange);border-color:var(--white)}
.btn-dark{left:663px;top:1891px;width:130px;height:32px;line-height:32px;background:var(--navy);color:var(--white);font-family:"Montserrat",sans-serif;font-size:12px;text-align:center}

/* blog */
.blog-card{width:282px;background:var(--card)}
.blog-card .thumb{width:282px;height:199px}
.blog-card .body{padding:18px 18px 0}
.blog-card h3{font-size:14px;font-weight:600;line-height:18px}
.blog-card p{font-size:12px;line-height:18px;color:var(--muted);margin-top:12px}
.blog-card .more{font-family:"Montserrat",sans-serif;font-size:12px;margin-top:20px;display:flex;align-items:center;gap:8px}
.blog-card .more.hot{color:var(--orange)}
.blog-card .more::before{content:"";width:12px;border-top:2px solid currentColor}

/* stores */
.store{top:2604px;width:134px;height:73px;background:var(--card);display:flex;align-items:center;justify-content:center;font-family:"Montserrat",sans-serif;font-size:21px;color:#333}
.round-arrow{top:2627px;width:28px;height:28px;border-radius:50%;display:flex;align-items:center;justify-content:center}

/* footer */
.footer{left:0;top:2759px;width:1200px;height:377px;background:var(--navy);color:#c5ccd4;font-size:13px}
.footer .label{font-size:13px;color:#aab3bd}
.footer .value{color:var(--white);font-size:16px;margin-top:2px}
.field{position:absolute;border:1px solid #7b8693;color:#c5ccd4;font-size:11px;padding:8px 12px}
.send{left:468px;top:231px;width:96px;height:34px;line-height:34px}
.footer .links{left:155px;top:346px;display:flex;gap:10px;font-size:11px}
.footer .links a{color:#c5ccd4;text-decoration:none}
.footer .links a.active{color:var(--orange)}
.badge{width:78px;height:22px;background:#5b6672;border-radius:3px}
</style>
</head>
<body>

<div class="abs topbar">
  <div class="abs contact">
    <span>&#9742; 1-555-014-2290</span><span>/</span><span>&#9993; support@parvento.com</span>
  </div>
  <div class="abs account">
    <span>&#128100; Login</span><span>/</span><span>&#10148; Register</span>
    <div class="social"><span></span><span class="hot"></span><span></span><span></span></div>
  </div>
</div>

<header class="abs header">
  <div class="abs logo">
    <div class="name"><i></i>parvento</div>
    <div class="tag">US shopping, global shipping</div>
  </div>
  <nav class="abs nav">
    <a class="active" href="#">Home</a><a href="#">Shipping Calculator</a><a href="#">How It Works</a><a href="#">Parvento Pricing</a><a href="#">Contact Us</a><a href="#">Learn More</a><a href="#">Blog</a>
  </nav>
</header>

<section class="abs hero">
  <div class="abs photo" role="img" aria-label="Passenger jet airliner flying through a cloudy blue sky"></div>
  <div class="abs tint"></div>
  <div class="abs frame"></div>
  <h1 class="abs">Fast Shipping?</h1>
  <p class="abs">When it's time to move out of your home or business, it's time to call <b>Parvento</b>. We make it easy.</p>
  <a class="abs btn-orange cta">Contact Us</a>
  <div class="abs arrow prev"><svg width="14" height="14" viewBox="0 0 14 14"><path d="M9 2 4 7l5 5" stroke="#fff" stroke-width="2.5" fill="none"/></svg></div>
  <div class="abs arrow next"><svg width="14" height="14" viewBox="0 0 14 14"><path d="M5 2l5 5-5 5" stroke="#fff" stroke-width="2.5" fill="none"/></svg></div>
</section>

<h2 class="abs section-title" style="top:642px">How Parvento Works<span class="divider"></span></h2>
<div class="abs steps">
  <div class="step">
    <div class="icon"><svg width="34" height="34" viewBox="0 0 34 34" fill="none" stroke="#fff" stroke-width="2.4"><path d="M17 30s-9-9-9-16a9 9 0 0 1 18 0c0 7-9 16-9 16z"/><circle cx="17" cy="14" r="3.5"/></svg></div>
    <p>Register for your free U.S. shopping address</p><span class="dot"></span>
  </div>
  <div class="step featured">
    <div class="icon"><svg width="36" height="36" viewBox="0 0 36 36" fill="none" stroke="#fff" stroke-width="2.4"><path d="M4 7h5l4 16h15l4-12H11"/><circle cx="15" cy="29" r="2"/><circle cx="26" cy="29" r="2"/></svg></div>
    <p>Shop anywhere<br>in the U.S</p><span class="dot"></span>
  </div>
  <div class="step">
    <div class="icon"><svg width="34" height="34" viewBox="0 0 34 34" fill="none" stroke="#fff" stroke-width="2.4"><rect x="7" y="13" width="20" height="15"/><path d="M7 13l4-6h12l4 6M17 7v6"/></svg></div>
    <p>Parvento receives your package and you get notified automatically</p><span class="dot"></span>
  </div>
  <div class="step">
    <div class="icon"><svg width="34" height="34" viewBox="0 0 34 34" fill="#fff"><path d="M30 5 4 16l9 3 3 10 4-7 7 5z"/></svg></div>
    <p>You choose how to ship your package anywhere in the world</p><span class="dot"></span>
  </div>
</div>

<div class="abs story-text">
  <h2>The Parvento Story<span class="divider"></span></h2>
  <p>Parvento is a leading company in the Package Forwarding industry. By leveraging the latest technologies and relationships with the world's top international shippers, Parvento provides tools to make shopping stores in the USA as easy as shopping at home. Whether you are shopping the USA for that new tablet for your business in Argentina or picking up some new fashions from your home...</p>
  <a class="btn-outline">Discover More</a>
</div>
<div class="abs story-media" role="img" aria-label="Globe with a cargo plane circling it on a golden background"></div>
<div class="abs play"><svg width="18" height="18" viewBox="0 0 18 18"><path d="M5 2l11 7-11 7z" fill="#fff"/></svg></div>

<div class="abs why-photo" role="img" aria-label="Airliner parked on a runway at sunset"></div>
<section class="abs why-panel">
  <h2>Why Use Parvento</h2><span class="divider"></span>
  <div class="reason" style="top:144px"><h3>Experience</h3><p>30 years experience in international shipping.</p></div>
  <div class="reason" style="top:215px"><h3>Value</h3><p>Discounted shipping rates with major carriers.</p></div>
  <div class="reason" style="top:286px"><h3>Trust</h3><p>Excellent customer service.</p></div>
  <div class="reason" style="top:359px"><h3>Savings</h3><p>No U.S. sales tax when using our New Hampshire</p></div>
</section>
<div class="abs why-icon" style="top:1566px"><svg width="26" height="26" viewBox="0 0 26 26" fill="none" stroke="#1f2833" stroke-width="2"><circle cx="13" cy="8" r="5"/><path d="M4 24c0-6 4-9 9-9s9 3 9 9z"/></svg></div>
<div class="abs why-icon" style="top:1637px"><svg width="26" height="26" viewBox="0 0 26 26" fill="none" stroke="#1f2833" stroke-width="2.2"><path d="M18 7c-1-2-3-3-5-3-3 0-5 2-5 4 0 5 10 3 10 9 0 2-2 4-5 4-2 0-4-1-5-3M13 1v24"/></svg></div>
<div class="abs why-icon hot" style="top:1708px"><svg width="28" height="28" viewBox="0 0 28 28" fill="none" stroke="#fff" stroke-width="2.2"><path d="M2 12l6-5 6 4 6-4 6 5-9 9a2 2 0 0 1-3 0z"/></svg></div>
<div class="abs why-icon" style="top:1781px"><svg width="26" height="26" viewBox="0 0 26 26" fill="none" stroke="#1f2833" stroke-width="2"><rect x="3" y="14" width="20" height="9" rx="2"/><circle cx="13" cy="7" r="5"/></svg></div>
<a class="abs btn-dark">Explore More</a>

<h2 class="abs section-title" style="top:2059px">Our Latest Blog<span class="divider"></span></h2>
<article class="abs blog-card" style="left:155px;top:2136px;height:389px">
  <div class="thumb" role="img" aria-label="Shipping container port with cranes and a plane overhead" style="background:linear-gradient(180deg,#8fb6d8 0%,#c6d8e6 45%,#b5573a 70%,#3d5f86 100%)"></div>
  <div class="body"><h3>Two International Shopping Days You'll Love</h3><p>If you're still recovering from the stress and pressure from the recent holidays, it's time to rest up and reset for...</p><div class="more hot">Read More</div></div>
</article>
<article class="abs blog-card" style="left:460px;top:2136px;height:389px">
  <div class="body" style="height:190px"><h3>2017 Fitness Shopping Trends &amp; Deals</h3><p>In the upcoming year, wearable tech, body weight training, and high-intensity interval training...</p><div class="more">Read More</div></div>
  <div class="thumb" role="img" aria-label="Airliner on a runway under an evening sky" style="background:linear-gradient(180deg,#3d6c9c 0%,#e5a157 55%,#5a514c 100%)"></div>
</article>
<article class="abs blog-card" style="left:763px;top:2136px;height:389px">
  <div class="thumb" role="img" aria-label="Freight truck driving on a highway" style="background:linear-gradient(180deg,#cfd7de 0%,#a3aab1 55%,#6f6a66 100%)"></div>
  <div class="body"><h3>End of Year Deals at Deep Discounts</h3><p>If you've been wondering if the 2016 holiday deals and steals will extend into 2017, the answer is yes...</p><div class="more">Read More</div></div>
</article>

<div class="abs round-arrow" style="left:103px;border:2px solid var(--orange)"><svg width="10" height="10" viewBox="0 0 10 10"><path d="M6 1 2 5l4 4" stroke="#f7941d" stroke-width="2" fill="none"/></svg></div>
<div class="abs store" style="left:171px">Little Oaks</div>
<div class="abs store" style="left:305px;font-weight:600;letter-spacing:4px">Hue</div>
<div class="abs store" style="left:439px;font-weight:700">Marketly</div>
<div class="abs store" style="left:573px">june lane</div>
<div class="abs store" style="left:707px">Craftly</div>
<div class="abs store" style="left:841px">Bidnest</div>
<div class="abs round-arrow" style="left:1067px;background:var(--orange)"><svg width="10" height="10" viewBox="0 0 10 10"><path d="M4 1l4 4-4 4" stroke="#fff" stroke-width="2" fill="none"/></svg></div>

<footer class="abs footer">
  <div class="abs" style="left:155px;top:42px">
    <div class="label">Call Us</div><div class="value">1-555-014-2290</div>
    <div class="label" style="margin-top:18px">Email</div><div style="color:#fff">support@parvento.com</div>
    <div class="label" style="margin-top:18px">Working hours:</div><div style="color:#fff">Monday - Friday &nbsp;9:00 am to 5:00 pm EST</div>
    <div class="label" style="margin-top:18px">Follow Us</div>
    <div style="display:flex;gap:10px;margin-top:6px"><span style="width:10px;height:10px;border-radius:50%;background:#fff"></span><span style="width:10px;height:10px;border-radius:50%;background:var(--orange)"></span><span style="width:10px;height:10px;border-radius:50%;background:#fff"></span><span style="width:10px;height:10px;border-radius:50%;background:#fff"></span></div>
  </div>
  <div class="abs heading" style="left:468px;top:48px;color:#fff;font-size:14px">Send A Message</div>
  <div class="field" style="left:468px;top:71px;width:278px;height:34px">Name</div>
  <div class="field" style="left:768px;top:71px;width:275px;height:34px">Email</div>
  <div class="field" style="left:468px;top:119px;width:575px;height:94px">Message</div>
  <div class="abs btn-orange send">&#10148; Send</div>
  <div class="abs" style="left:155px;top:316px;font-size:12px">© 2017 &nbsp;parvento. All Rights Reserved.</div>
  <div class="abs links"><a class="active">How It Works</a>/<a>Pricing</a>/<a>Terms of Service</a>/<a>Privacy Policy</a>/<a>Contact Us</a></div>
  <div class="abs" style="left:686px;top:330px;display:flex;align-items:center;gap:18px;font-size:12px">In Partnership With <span class="badge"></span><span class="badge" style="width:90px"></span><span class="badge" style="width:56px"></span></div>
</footer>

</body>
</html>
```